Tennis coaching business requires a dynamic flyer

I need a front and back flyer encouraging people to sign up for tennis lessons using engaging pictures and text. My business provides tennis coaching for adults and kids, group lessons, private and semi private lessons, Quick Rally and Pulse Court. I would like similar colours to my logo(greens and blacks) but am open to different designs. I will upload my business card as a logo reference and also a basic flyer I designed years ago which will roughly outline what I do. I will also upload a few pics from my website www.brightcourtlessons.com.au.
Pulse Court is a fitness workout to music whilst learning to play tennis and is a fantastic way to keep/get fit.
Quick Rally Tennis is a modified coaching program for kids at a beginner to intermediate level.

Target Market(s)

The target market is parents with young kids aged 5+, but both parents and kids should see the flyer and be engaged.

Industry/Entity Type

Business

Font styles to use
Serif

Requirements
Must have
• Eyecatching design, I'd like the flyer both front and back to have one of the uploaded pics as the print background if possible, rather than just plain colour background with text overlay. I'd also like the flyer to include that it's a locally run tennis coaching business with over 15years experience. Front must include the free racquet offer and the Kelbrook Quick Rally graphic. I also offer a free trial lesson to anyone interested in doing tennis lessons so I'd like that included also. My name, phone number and website details should be at the bottom of front and back.

```html
<!DOCTYPE html>
<html lang="en">
<head>
<meta charset="utf-8">
<title>Brightcourt Lessons – Flyer Front and Back</title>
<link rel="stylesheet" href="https://fonts.googleapis.com/css2?family=Oswald:wght@400;500;700&family=Roboto+Condensed:ital,wght@0,400;0,700;1,400&family=Exo+2:ital,wght@1,800&display=swap">
<style>
  :root{
    --bg:#e8e5e1;
    --ink-dark:#242424;
    --ink-darker:#161616;
    --green:#8cbf26;
    --green-light:#b3d94a;
    --green-deep:#5f8f12;
    --orange:#f7ae1c;
    --pink:#de2a7c;
    --red:#d32a2a;
    --note:#f6e15a;
    --note-deep:#eac728;
    --text:#474747;
    --white:#ffffff;
  }
  *{box-sizing:border-box;margin:0;padding:0}
  html,body{width:1200px;height:907px;overflow:hidden;background:var(--bg)}
  body{position:relative;font-family:"Roboto Condensed",sans-serif}

  .flyer{position:absolute;width:482px;height:681px;overflow:hidden;background:var(--ink-dark);box-shadow:0 6px 18px rgba(0,0,0,.28)}
  .flyer--front{left:74px;top:59px}
  .flyer--back{left:614px;top:120px}
  .flyer svg.layer{position:absolute;left:0;top:0;width:482px;height:681px}

  .brand{position:absolute;left:14px;top:16px;display:flex;align-items:center;gap:7px}
  .brand__dot{width:22px;height:22px;border-radius:50%;background:var(--green)}
  .brand__name{font-family:"Roboto Condensed",sans-serif;font-weight:700;font-size:17px;color:var(--white);text-transform:uppercase;letter-spacing:.5px;white-space:nowrap}

  .trial-ribbon{position:absolute;left:26px;top:354px;width:232px;height:38px;background:var(--orange);
    clip-path:polygon(0 0,100% 0,94% 50%,100% 100%,0 100%,4% 85%,0 70%,4% 55%,0 40%,4% 25%,0 12%);
    font-family:"Oswald",sans-serif;font-weight:500;font-size:24px;color:var(--white);line-height:38px;padding-left:16px;letter-spacing:.3px;white-space:nowrap}

  .partner{position:absolute;left:276px;top:336px;width:190px;display:flex;align-items:center;gap:8px}
  .partner__dot{flex:none;width:14px;height:14px;border-radius:50%;background:var(--pink)}
  .partner__name{font-family:"Oswald",sans-serif;font-weight:700;font-size:22px;line-height:25px;color:var(--pink);text-transform:uppercase;white-space:nowrap}

  .tagline{position:absolute;left:12px;top:405px;width:440px;font-family:"Exo 2",sans-serif;font-style:italic;font-weight:800;font-size:15.5px;line-height:19px;color:var(--green);text-transform:uppercase}

  .ticks{position:absolute;list-style:none}
  .ticks li{display:flex;align-items:center;gap:9px;text-transform:uppercase;color:var(--text);font-size:13.5px;white-space:nowrap}
  .ticks svg{flex:none;width:13px;height:13px}
  .ticks--front{left:12px;top:451px}
  .ticks--front li{height:23.4px}
  .ticks--back{left:267px;top:503px}
  .ticks--back li{height:22.5px;font-size:12.5px;color:#3a3a3a}

  .offer-note{position:absolute;left:322px;top:462px;width:138px;height:124px;transform:rotate(-6deg);
    background:linear-gradient(160deg,var(--note),var(--note-deep));box-shadow:2px 4px 8px rgba(0,0,0,.3);padding:10px 8px}
  .offer-note__pin{position:absolute;left:62px;top:-5px;width:11px;height:11px;border-radius:50%;background:var(--green-deep)}
  .offer-note__art{position:absolute;left:6px;top:12px;width:36px;height:36px;border-radius:50%;background:radial-gradient(circle,#f3d98e,#c9914a)}
  .offer-note__title{margin-left:38px;margin-top:8px;font-family:"Oswald",sans-serif;font-weight:500;font-size:15px;line-height:18px;color:var(--red);white-space:nowrap}
  .offer-note__sub{margin-left:50px;font-family:"Oswald",sans-serif;font-size:6.5px;color:var(--green-deep);text-transform:uppercase;white-space:nowrap}
  .offer-note__body{margin-top:14px;font-family:"Oswald",sans-serif;font-size:8.2px;line-height:11px;color:#2a2a2a;text-transform:uppercase}

  .contact{position:absolute;right:12px;bottom:10px;text-align:right;line-height:15.5px;white-space:nowrap}
  .contact__name{font-family:"Roboto Condensed",sans-serif;font-weight:700;font-size:14px;color:var(--white);text-transform:uppercase}
  .contact__phone,.contact__web{font-size:13px;color:var(--green)}
  .contact__phone svg{width:7px;height:7px;margin-left:3px}
  .contact__web::after{content:"";display:inline-block;width:5px;height:5px;border-radius:50%;background:var(--green);margin-left:5px;vertical-align:middle}

  .social{position:absolute;left:12px;bottom:13px;display:flex;align-items:center;gap:8px}
  .social__dot{width:10px;height:10px;background:var(--green-light)}
  .social__text{font-size:7.4px;line-height:9px;color:var(--white)}

  .about{position:absolute;left:12px;top:372px;width:216px;font-size:10.2px;line-height:12.6px;color:var(--white);text-align:justify}
  .about p+p{margin-top:10px}
  .about strong{font-weight:700}
  .about .program{color:var(--green-light)}
  .experience{position:absolute;left:13px;top:540px;width:218px;font-family:"Oswald",sans-serif;font-weight:500;font-size:18px;line-height:24px;color:var(--green-light);white-space:nowrap}

  .pulse{position:absolute;left:272px;top:378px;width:184px;display:flex;align-items:center;justify-content:center;gap:8px}
  .pulse__dot{flex:none;width:14px;height:14px;border-radius:50%;background:var(--pink)}
  .pulse__name{font-family:"Oswald",sans-serif;font-weight:700;font-size:28px;line-height:34px;color:var(--pink);text-transform:uppercase;white-space:nowrap}
  .junior-title{position:absolute;left:262px;top:462px;font-family:"Roboto Condensed",sans-serif;font-style:italic;font-weight:400;font-size:25px;line-height:30px;color:var(--green);text-transform:uppercase;white-space:nowrap}
</style>
</head>
<body>

<section class="flyer flyer--front">
  <svg class="layer" viewBox="0 0 482 681" aria-hidden="true">
    <defs>
      <linearGradient id="fDark" x1="0" y1="0" x2="0" y2="1"><stop offset="0" stop-color="#2e2e2e"/><stop offset="1" stop-color="#1b1b1b"/></linearGradient>
    </defs>
    <rect width="482" height="681" fill="url(#fDark)"/>
  </svg>
  <svg class="layer" viewBox="0 0 482 681" role="img" aria-label="Photo of a smiling coach standing with two young girls on a tennis court">
    <defs>
      <linearGradient id="fPhoto" x1="0" y1="0" x2="1" y2="1"><stop offset="0" stop-color="#5d6a34"/><stop offset=".45" stop-color="#9b5a3e"/><stop offset="1" stop-color="#8f8a82"/></linearGradient>
    </defs>
    <path d="M0,170 C130,95 300,40 482,10 L482,250 C330,290 150,300 0,288 Z" fill="url(#fPhoto)"/>
  </svg>
  <svg class="layer" viewBox="0 0 482 681" aria-hidden="true">
    <defs>
      <linearGradient id="fGreen" x1="0" y1="0" x2="1" y2="0"><stop offset="0" stop-color="#6d9e15"/><stop offset=".5" stop-color="#b3d94a"/><stop offset="1" stop-color="#7fb21d"/></linearGradient>
    </defs>
    <path d="M0,160 C130,85 300,30 482,2 L482,12 C300,42 130,98 0,174 Z" fill="url(#fGreen)"/>
    <path d="M0,282 C150,298 330,286 482,240 L482,300 C330,330 150,336 0,325 Z" fill="url(#fGreen)"/>
    <path d="M0,316 C150,330 330,316 482,262 L482,604 C330,590 150,602 0,612 Z" fill="#ffffff"/>
    <path d="M120,600 C260,586 380,580 482,586 L482,596 C380,592 260,596 120,604 Z" fill="url(#fGreen)"/>
  </svg>

  <div class="brand"><span class="brand__dot"></span><span class="brand__name">Brightcourt Lessons</span></div>

  <div class="trial-ribbon">FREE TRIAL LESSON</div>
  <div class="partner"><span class="partner__dot"></span><span class="partner__name">Kelbrook<br>Quick Rally</span></div>

  <p class="tagline">Everyone is different, and the approach<br>to coaching should cater for that</p>

  <ul class="ticks ticks--front">
    <li><svg viewBox="0 0 14 14"><circle cx="7" cy="7" r="7" fill="#8cbf26"/><path d="M3.8,7.2 6,9.3 10.3,4.8" stroke="#fff" stroke-width="1.8" fill="none"/></svg>All standards from beginner to advanced</li>
    <li><svg viewBox="0 0 14 14"><circle cx="7" cy="7" r="7" fill="#8cbf26"/><path d="M3.8,7.2 6,9.3 10.3,4.8" stroke="#fff" stroke-width="1.8" fill="none"/></svg>Private, semi private and group lessons</li>
    <li><svg viewBox="0 0 14 14"><circle cx="7" cy="7" r="7" fill="#8cbf26"/><path d="M3.8,7.2 6,9.3 10.3,4.8" stroke="#fff" stroke-width="1.8" fill="none"/></svg>All ages catered for</li>
    <li><svg viewBox="0 0 14 14"><circle cx="7" cy="7" r="7" fill="#8cbf26"/><path d="M3.8,7.2 6,9.3 10.3,4.8" stroke="#fff" stroke-width="1.8" fill="none"/></svg>Very affordable</li>
    <li><svg viewBox="0 0 14 14"><circle cx="7" cy="7" r="7" fill="#8cbf26"/><path d="M3.8,7.2 6,9.3 10.3,4.8" stroke="#fff" stroke-width="1.8" fill="none"/></svg>Qualified, enthusiastic coaches</li>
    <li><svg viewBox="0 0 14 14"><circle cx="7" cy="7" r="7" fill="#8cbf26"/><path d="M3.8,7.2 6,9.3 10.3,4.8" stroke="#fff" stroke-width="1.8" fill="none"/></svg>Quick Rally and Pulse Court</li>
  </ul>

  <div class="offer-note">
    <span class="offer-note__pin"></span>
    <div class="offer-note__art" role="img" aria-label="Illustration of a tennis racquet"></div>
    <p class="offer-note__title">FREE OFFER</p>
    <p class="offer-note__sub">Tennis racquet</p>
    <p class="offer-note__body">Anyone under 12 signing up for their 1st term of coaching receives a free tennis racquet!!!</p>
  </div>

  <div class="social"><span class="social__dot"></span><span class="social__text">Like us on ClubFeed at<br>Brightcourt Lessons</span></div>
  <div class="contact">
    <p class="contact__name">Dan Whitford</p>
    <p class="contact__phone">0400 555 218<svg viewBox="0 0 10 10"><path d="M2,1 4,3 3,4.3 C4,6 4.5,6.5 5.7,7 L7,6 9,8 7.6,9.4 C4,9 1,6 0.6,2.4 Z" fill="#8cbf26"/></svg></p>
    <p class="contact__web">www.brightcourtlessons.com.au</p>
  </div>
</section>

<section class="flyer flyer--back">
  <svg class="layer" viewBox="0 0 482 681" aria-hidden="true">
    <defs>
      <linearGradient id="bDark" x1="0" y1="0" x2="0" y2="1"><stop offset="0" stop-color="#2e2e2e"/><stop offset="1" stop-color="#1b1b1b"/></linearGradient>
    </defs>
    <rect width="482" height="681" fill="url(#bDark)"/>
  </svg>
  <svg class="layer" viewBox="0 0 482 681" role="img" aria-label="Photo of a boy in a red shirt hitting a forehand in front of a hedge">
    <defs>
      <linearGradient id="bPhoto" x1="0" y1="0" x2="1" y2="1"><stop offset="0" stop-color="#2f4a1e"/><stop offset=".5" stop-color="#556b35"/><stop offset="1" stop-color="#3b3f33"/></linearGradient>
    </defs>
    <path d="M0,160 C130,88 300,32 482,3 L482,250 C330,290 150,308 0,302 Z" fill="url(#bPhoto)"/>
  </svg>
  <svg class="layer" viewBox="0 0 482 681" aria-hidden="true">
    <defs>
      <linearGradient id="bGreen" x1="0" y1="0" x2="1" y2="0"><stop offset="0" stop-color="#6d9e15"/><stop offset=".5" stop-color="#b3d94a"/><stop offset="1" stop-color="#7fb21d"/></linearGradient>
    </defs>
    <path d="M0,150 C130,80 300,24 482,-4 L482,6 C300,36 130,92 0,164 Z" fill="url(#bGreen)"/>
    <path d="M0,296 C150,306 330,290 482,244 L482,300 C330,330 150,344 0,340 Z" fill="url(#bGreen)"/>
    <path d="M0,336 C150,340 330,326 482,282 L482,604 C330,590 150,604 0,614 Z" fill="#ffffff"/>
    <rect x="0" y="338" width="245" height="272" fill="#262626"/>
    <path d="M245,596 C340,584 420,578 482,574 L482,590 C420,592 340,596 245,604 Z" fill="url(#bGreen)"/>
  </svg>
  <svg class="layer" viewBox="0 0 482 681" role="img" aria-label="Round photo of a smiling young girl">
    <defs>
      <radialGradient id="bPortrait"><stop offset="0" stop-color="#f2c9a6"/><stop offset="1" stop-color="#caa266"/></radialGradient>
    </defs>
    <circle cx="395" cy="265" r="67" fill="url(#bPortrait)" stroke="#ffffff" stroke-width="5"/>
  </svg>

  <div class="brand"><span class="brand__dot"></span><span class="brand__name">Brightcourt Lessons</span></div>

  <div class="about">
    <p><strong>Brightcourt Lessons strives to provide a fun, positive and challenging environment for people of all walks of life to learn and enjoy tennis.</strong></p>
    <p><span class="program">Pulse Court</span> is a fitness workout to music whilst learning to play tennis and is a fantastic way to keep/get fit.</p>
    <p><span class="program">Quick Rally Tennis</span> is a modified coaching program for kids at a beginner to intermediate level.</p>
  </div>
  <p class="experience">OVER 15 YEARS EXPERIENCE!</p>

  <div class="pulse"><span class="pulse__dot"></span><span class="pulse__name">Pulse Court</span></div>
  <h2 class="junior-title">Junior Coaching</h2>
  <ul class="ticks ticks--back">
    <li><svg viewBox="0 0 14 14"><circle cx="7" cy="7" r="7" fill="#8cbf26"/><path d="M3.8,7.2 6,9.3 10.3,4.8" stroke="#fff" stroke-width="1.8" fill="none"/></svg>Group lessons</li>
    <li><svg viewBox="0 0 14 14"><circle cx="7" cy="7" r="7" fill="#8cbf26"/><path d="M3.8,7.2 6,9.3 10.3,4.8" stroke="#fff" stroke-width="1.8" fill="none"/></svg>Private / semi private lessons</li>
    <li><svg viewBox="0 0 14 14"><circle cx="7" cy="7" r="7" fill="#8cbf26"/><path d="M3.8,7.2 6,9.3 10.3,4.8" stroke="#fff" stroke-width="1.8" fill="none"/></svg>In house round robin play</li>
  </ul>

  <div class="social"><span class="social__dot"></span><span class="social__text">Like us on ClubFeed at<br>Brightcourt Lessons</span></div>
  <div class="contact">
    <p class="contact__name">Dan Whitford</p>
    <p class="contact__phone">0400 555 218<svg viewBox="0 0 10 10"><path d="M2,1 4,3 3,4.3 C4,6 4.5,6.5 5.7,7 L7,6 9,8 7.6,9.4 C4,9 1,6 0.6,2.4 Z" fill="#8cbf26"/></svg></p>
    <p class="contact__web">www.brightcourtlessons.com.au</p>
  </div>
</section>

</body>
</html>
```